Pregnancy and Fertility Information Website

Hello Designers,
I need a website which provide tips and information about healthy and happy pregnancy. My website name is Lorvin medical.

The website should provide all the information needed throughout pregnancy and beyond ranging from pregnancy tracking tools and articles about common pregnancy concerns and what to expect during pregnancy,etc.
The details about first trimester, second trimester and third trimester should be highlighted in the website.

Top Navigation
Home, Fertility, Pregnancy basics, Articles, Tips and News

I'm looking for a simple and clean design which involves captivating images and colors but it shouldn't be crowded. The design must be professional and modern. An easy to navigate layout is a must.

Green, violet, blue and light yellow colors are my favorites but i'm open to other options.

Any questions. Kindly ask

Industry/Entity Type

Medical

```html
<!DOCTYPE html>
<html lang="en">
<head>
<meta charset="utf-8">
<title>Lorvin Medical – Pregnancy &amp; Fertility</title>
<link href="https://fonts.googleapis.com/css2?family=Open+Sans:wght@400;600;700&family=Raleway:wght@400;500;600&display=swap" rel="stylesheet">
<style>
:root{
  --navy:#0d1646;
  --navy-2:#141d52;
  --green:#97c800;
  --violet:#b383d9;
  --light:#f3f3f3;
  --cream:#f4f1bd;
  --ink:#111;
  --social:#1976c0;
  --white:#fff;
}
*{box-sizing:border-box;margin:0;padding:0}
html,body{width:1200px;height:2571px;overflow:hidden}
body{font-family:"Open Sans",Arial,sans-serif;color:var(--ink);background:var(--white);position:relative}

/* top bar */
.topbar{position:absolute;left:0;top:0;width:1200px;height:38px;background:var(--navy);color:var(--white);font-size:13px;display:flex;align-items:center;padding:0 70px}
.topbar span{margin-right:22px;display:flex;align-items:center;gap:6px}
.topbar .social{position:absolute;right:70px;top:8px;display:flex;gap:4px}
.sq{display:block;background:var(--social)}
.topbar .sq{width:22px;height:22px}

/* header */
.header{position:absolute;left:0;top:38px;width:1200px;height:120px;background:var(--white)}
.brand{position:absolute;left:77px;top:44px;display:flex;align-items:center;gap:10px;font-family:"Open Sans",sans-serif;font-weight:600;font-size:24px;color:var(--navy)}
.brand i{display:block;width:30px;height:30px;border-radius:50%;background:var(--social)}
.nav{position:absolute;right:82px;top:0;display:flex;gap:32px;height:110px;align-items:center;font-size:16px;font-weight:600;color:var(--navy)}
.nav a{color:inherit;text-decoration:none;position:relative}
.nav a.active{color:var(--green)}
.nav a.active::before{content:"";position:absolute;left:-6px;right:-6px;top:-40px;height:4px;background:var(--green)}

/* hero */
.hero{position:absolute;left:0;top:158px;width:1200px;height:463px;background:linear-gradient(90deg,#0d1646 0%,#1e2c66 45%,#3a4a7e 100%)}
.hero-photo{position:absolute;left:94px;top:0;width:300px;height:463px;background:radial-gradient(ellipse at 50% 55%,#e9e3df 0%,#b9c3d8 45%,rgba(13,22,70,0) 75%)}
.hero-title{position:absolute;left:596px;top:84px;width:262px;font-family:"Raleway",sans-serif;font-weight:500;font-size:32px;line-height:46px;color:var(--white);letter-spacing:.5px;white-space:nowrap}
.hero-green{position:absolute;left:866px;top:20px;width:257px;height:213px;background:var(--green);color:var(--white);padding:18px 17px}
.hero-green h3{font-family:"Raleway",sans-serif;font-weight:600;font-size:20px;display:inline-block;border-bottom:2px solid var(--white);padding-bottom:2px;margin-bottom:10px}
.hero-green p{font-size:11px;line-height:17px}
.hero-list{position:absolute;left:866px;top:233px;width:257px;height:209px;background:var(--white);padding:22px 17px}
.hero-list h3{font-family:"Raleway",sans-serif;font-weight:600;font-size:20px;color:var(--navy);display:inline-block;border-bottom:2px solid var(--navy);margin-bottom:14px}
.hero-list li{list-style:none;display:flex;align-items:center;gap:12px;font-size:15px;color:var(--navy);margin-bottom:19px}
.hero-list li b{display:block;width:14px;height:14px;border:1.5px solid var(--navy);position:relative}
.hero-list li b::after{content:"";position:absolute;left:3px;top:3px;width:5px;height:5px;background:var(--navy)}
.contact-box{position:absolute;left:607px;top:233px;width:259px;height:209px;background:var(--navy);color:var(--white);padding:18px 16px}
.contact-box h3{font-family:"Raleway",sans-serif;font-weight:500;font-size:21px;margin-bottom:14px}
.contact-box p{font-size:10.5px;line-height:17px}
.btn{display:inline-block;border:1.5px solid var(--white);color:var(--white);font-size:15px;text-align:center}
.contact-box .btn{position:absolute;left:72px;top:148px;width:110px;height:36px;line-height:33px}

/* section titles */
.sec-title{position:absolute;left:0;width:1200px;text-align:center;font-family:"Raleway",sans-serif;font-weight:500}
.divider{position:absolute;left:377px;width:497px;height:4px;background:#d6d6d6}
.divider::after{content:"";position:absolute;left:155px;width:185px;height:4px;background:var(--green)}

/* welcome */
.welcome{position:absolute;left:0;top:621px;width:1200px;height:390px;background:var(--violet);color:var(--white)}
.welcome .sec-title{top:32px;font-size:31px}
.welcome .divider{top:88px;background:#ecebf2}
.welcome .divider::after{background:#3a3f6e}
.welcome .col{position:absolute;top:125px;font-size:15.5px;line-height:21px}
.welcome .col small{display:block;font-size:13.5px;line-height:21px}

/* trimesters */
.trimesters{position:absolute;left:0;top:1011px;width:1200px;height:638px;background:var(--light)}
.trimesters .sec-title{top:44px;font-size:29px;color:var(--navy)}
.trimesters .divider{top:98px}
.card{position:absolute;top:167px;width:280px;height:250px}
.card .back{position:absolute;left:0;top:0;width:260px;height:240px;background:var(--green);border:2px solid #ddd}
.card .photo{position:absolute;left:15px;top:14px;width:264px;height:236px;background:var(--white);padding:4px;box-shadow:0 0 0 1px #ccc}
.card .photo div{width:100%;height:100%;background:linear-gradient(90deg,#29306a 0%,#3a4580 55%,#9aa0b8 85%,#c7c3c4 100%)}
.card h4{position:absolute;left:35px;top:38px;font-family:"Open Sans",sans-serif;font-weight:600;font-size:21px;line-height:27px;color:var(--white)}
.card-text{position:absolute;top:446px;width:270px;font-size:13.5px;line-height:20.5px;color:var(--ink)}

/* services */
.services{position:absolute;left:0;top:1649px;width:1200px;height:466px;background:var(--white)}
.services .sec-title{top:34px;font-size:29px;color:var(--navy)}
.services .divider{top:92px;left:364px;width:523px}
.svc{position:absolute;width:320px;height:90px}
.svc svg{position:absolute;left:0;top:6px;width:46px;height:46px}
.svc h4{position:absolute;left:67px;top:0;font-weight:400;font-size:22px;color:var(--ink)}
.svc p{position:absolute;left:67px;top:36px;width:200px;font-size:12px;line-height:16px}

/* CTA */
.cta{position:absolute;left:0;top:2115px;width:1200px;height:110px;background:var(--navy);color:var(--white)}
.cta p{position:absolute;left:70px;top:36px;font-size:28px;letter-spacing:.5px}
.cta .btn{position:absolute;left:924px;top:30px;width:162px;height:50px;line-height:47px;font-size:15px}

/* footer */
.footer{position:absolute;left:0;top:2225px;width:1200px;height:298px;background:var(--cream)}
.footer h5{position:absolute;font-size:20px;font-weight:700;color:var(--ink)}
.footer .about{position:absolute;left:70px;top:106px;width:380px;font-size:16px;line-height:26px}
.footer .profiles{position:absolute;left:70px;top:175px;font-size:15px;display:flex;align-items:center;gap:24px}
.footer .profiles .icons{display:flex;gap:10px}
.footer .profiles .sq{width:32px;height:32px}
.footer .links{position:absolute;left:525px;top:110px;list-style:none;font-size:15px;line-height:25px}
.footer .details{position:absolute;left:797px;top:110px;font-size:15px;line-height:25px}
.footer .details .row{display:flex}
.footer .details .lbl{width:105px}
.footer .details .val{display:flex;gap:8px}
.footer .details svg{flex:none;margin-top:6px}
.copy{position:absolute;left:0;top:2523px;width:1200px;height:48px;background:var(--navy);color:var(--white);font-size:14px;text-align:center;line-height:48px}
</style>
</head>
<body>

<div class="topbar">
  <span>Have any questions?</span>
  <span><svg width="12" height="12" viewBox="0 0 12 12"><path d="M2 1l2 0 1 3-1.3 1a6 6 0 0 0 3.3 3.3L8 7l3 1v2c0 .6-.4 1-1 1A9 9 0 0 1 1 2c0-.6.4-1 1-1z" fill="#fff"/></svg>+11 555 010 270</span>
  <span><svg width="14" height="10" viewBox="0 0 14 10"><rect x=".5" y=".5" width="13" height="9" fill="none" stroke="#fff"/><path d="M.5.5l6.5 5 6.5-5" fill="none" stroke="#fff"/></svg>hello@lorvinmedical.example</span>
  <div class="social"><i class="sq"></i><i class="sq"></i><i class="sq"></i></div>
</div>

<header class="header">
  <div class="brand"><i></i>Lorvin Medical</div>
  <nav class="nav">
    <a class="active" href="#">Home</a>
    <a href="#">Fertility</a>
    <a href="#">Pregnancy Basics</a>
    <a href="#">Articles</a>
    <a href="#">Tips and News</a>
  </nav>
</header>

<section class="hero">
  <div class="hero-photo" role="img" aria-label="Doctor with clipboard examining a smiling pregnant woman in a clinic"></div>
  <h1 class="hero-title">Welcome to<br>Lorvin Medical</h1>
  <div class="hero-green">
    <h3>Lorvin Medical</h3>
    <p>Lorem Ipsum Text Here Lorem Ipsum Text Here Lorem Ipsum Text Here Lorem Ipsum Text Here Lorem Ipsum Text Here Lorem Ipsum Text Here Lorem Ipsum Text Here Lorem Ipsum Text Here</p>
  </div>
  <div class="contact-box">
    <h3>Contact us</h3>
    <p>Lorvin Medical<br>Level 12, 48 Harbour Lane,<br>Northvale, Victoria 3000<br>Australia</p>
    <span class="btn">Contact</span>
  </div>
  <div class="hero-list">
    <h3>Lorem Ipsum :</h3>
    <ul>
      <li><b></b>First Trimester</li>
      <li><b></b>Second Trimester</li>
      <li><b></b>Third Trimester</li>
    </ul>
  </div>
</section>

<section class="welcome">
  <h2 class="sec-title">Welcome to Lorvin Medical</h2>
  <div class="divider"></div>
  <div class="col" style="left:70px;width:545px">Lorem Ipsum is simply dummy text of the printing and typesetting industry. Lorem Ipsum has been the industry's standard dummy text ever since the 1500s, when an unknown printer took a galley of type and scrambled it to make a type specimen book.<small>Lorem Ipsum is simply dummy text of the printing and typesetting industry. Lorem Ipsum has been the industry's standard dummy text ever since the 1500s, when an unknown printer took a galley of type and scrambled it to make a type specimen book.</small></div>
  <div class="col" style="left:646px;width:470px">Lorem Ipsum is simply dummy text of the printing and typesetting industry. Lorem Ipsum has been the industry's standard dummy text ever since the 1500s, when an unknown printer took a galley of type and scrambled it to make a type specimen book.<small>Lorem Ipsum is simply dummy text of the printing and typesetting industry. Lorem Ipsum has been the industry's standard dummy text ever since the 1500s, when an unknown printer took a galley of type and scrambled it to make a type specimen book.</small></div>
</section>

<section class="trimesters">
  <h2 class="sec-title">Lorem Ipsum</h2>
  <div class="divider"></div>

  <div class="card" style="left:70px">
    <div class="back"></div>
    <div class="photo"><div role="img" aria-label="Woman in early pregnancy on a dark blue patterned backdrop"></div></div>
    <h4>First<br>Trimester</h4>
  </div>
  <p class="card-text" style="left:70px">Lorem Ipsum is simply dummy text of the printing and typesetting industry. Lorem Ipsum has been the industry's standard dummy text ever since the 1500s, when an unknown printer took a galley of type and scrambled it to make a type specimen book.</p>

  <div class="card" style="left:456px">
    <div class="back"></div>
    <div class="photo"><div role="img" aria-label="Pregnant belly in a grey dress on a dark blue patterned backdrop"></div></div>
    <h4>Second<br>Trimester</h4>
  </div>
  <p class="card-text" style="left:460px">Lorem Ipsum is simply dummy text of the printing and typesetting industry. Lorem Ipsum has been the industry's standard dummy text ever since the 1500s, when an unknown printer took a galley of type and scrambled it to make a type specimen book.</p>

  <div class="card" style="left:845px">
    <div class="back"></div>
    <div class="photo"><div role="img" aria-label="Woman in late pregnancy holding her belly on a dark blue patterned backdrop"></div></div>
    <h4>Third<br>Trimester</h4>
  </div>
  <p class="card-text" style="left:846px">Lorem Ipsum is simply dummy text of the printing and typesetting industry. Lorem Ipsum has been the industry's standard dummy text ever since the 1500s, when an unknown printer took a galley of type and scrambled it to make a type specimen book.</p>
</section>

<section class="services">
  <h2 class="sec-title">See what we provide for your health</h2>
  <div class="divider"></div>

  <div class="svc" style="left:70px;top:155px">
    <svg viewBox="0 0 46 46"><circle cx="23" cy="13" r="9" fill="#111"/><path d="M4 44c0-12 8-19 19-19s19 7 19 19z" fill="#111"/></svg>
    <h4>Certified doctors</h4><p>Vitae adipiscing turpis. Aenean ligula nibh in, molestie id viverra a, dapibus at dolor.</p>
  </div>
  <div class="svc" style="left:470px;top:155px">
    <svg viewBox="0 0 46 46"><rect x="9" y="6" width="28" height="36" rx="2" fill="none" stroke="#111" stroke-width="3"/><rect x="17" y="3" width="12" height="6" fill="#111"/><path d="M15 18h16M15 25h16M15 32h16" stroke="#111" stroke-width="2.5"/></svg>
    <h4>Quick visits</h4><p>Vitae adipiscing turpis. Aenean ligula nibh in, molestie id viverra a, dapibus at dolor.</p>
  </div>
  <div class="svc" style="left:854px;top:155px">
    <svg viewBox="0 0 46 46"><rect x="1" y="10" width="44" height="26" rx="2" fill="#111"/><rect x="1" y="15" width="44" height="4" fill="#fff"/><rect x="6" y="26" width="14" height="3" fill="#fff"/></svg>
    <h4>Card payments</h4><p>Vitae adipiscing turpis. Aenean ligula nibh in, molestie id viverra a, dapibus at dolor.</p>
  </div>
  <div class="svc" style="left:70px;top:322px">
    <svg viewBox="0 0 46 46"><path d="M8 6h30l4 12H4z" fill="#111"/><rect x="4" y="20" width="38" height="22" fill="#111"/><rect x="17" y="26" width="12" height="4" fill="#fff"/></svg>
    <h4>Patients history</h4><p>Vitae adipiscing turpis. Aenean ligula nibh in, molestie id viverra a, dapibus at dolor.</p>
  </div>
  <div class="svc" style="left:470px;top:322px">
    <svg viewBox="0 0 46 46"><path d="M6 40C8 20 22 8 42 6c-2 20-14 32-32 32z" fill="#111"/><path d="M4 44L30 18" stroke="#fff" stroke-width="2"/></svg>
    <h4>Natural medicine</h4><p>Vitae adipiscing turpis. Aenean ligula nibh in, molestie id viverra a, dapibus at dolor.</p>
  </div>
  <div class="svc" style="left:854px;top:322px">
    <svg viewBox="0 0 46 46"><circle cx="23" cy="25" r="17" fill="none" stroke="#111" stroke-width="3"/><path d="M23 14v11l7 5" fill="none" stroke="#111" stroke-width="3"/><path d="M6 10l8-6M40 10l-8-6" stroke="#111" stroke-width="3"/></svg>
    <h4>Short terms</h4><p>Vitae adipiscing turpis. Aenean ligula nibh in, molestie id viverra a, dapibus at dolor.</p>
  </div>
</section>

<section class="cta">
  <p>Do you want to visit our clinic? Make an free appointment!</p>
  <span class="btn">Contact Us</span>
</section>

<footer class="footer">
  <h5 style="left:70px;top:52px;display:flex;align-items:center;gap:12px">Lorvin Medical :<i style="display:block;width:26px;height:26px;border-radius:50%;background:var(--social)"></i></h5>
  <p class="about">Vitae adipiscing turpis. Aenean ligula nibh in, molestie id viverra a, dapibus at dolor.</p>
  <div class="profiles">Our profiles in Social Media :<span class="icons"><i class="sq"></i><i class="sq"></i><i class="sq"></i></span></div>

  <h5 style="left:525px;top:55px">Quick Links :</h5>
  <ul class="links"><li>Home</li><li>Fertility</li><li>Pregnancy Basics</li><li>Articles</li><li>Tips and News</li></ul>

  <h5 style="left:797px;top:55px">Contact Details :</h5>
  <div class="details">
    <div class="row"><span class="lbl">Email :</span><span class="val"><svg width="16" height="11" viewBox="0 0 16 11"><rect x=".5" y=".5" width="15" height="10" fill="none" stroke="#111"/><path d="M.5.5l7.5 6 7.5-6" fill="none" stroke="#111"/></svg>hello@lorvinmedical.example</span></div>
    <div class="row"><span class="lbl">Quick Call :</span><span class="val"><svg width="14" height="14" viewBox="0 0 14 14"><rect width="14" height="14" rx="2" fill="#111"/><path d="M4 3h1.5l.8 2-1 .8a4 4 0 0 0 2.2 2.2l.8-1 2 .8V10c0 .5-.3.8-.8.8A6.5 6.5 0 0 1 3.2 3.8c0-.5.3-.8.8-.8z" fill="#fff"/></svg>+11 555 010 270</span></div>
    <div class="row"><span class="lbl">Location :</span><span class="val"><svg width="12" height="16" viewBox="0 0 12 16"><path d="M6 0a6 6 0 0 1 6 6c0 4-6 10-6 10S0 10 0 6a6 6 0 0 1 6-6z" fill="#111"/><circle cx="6" cy="6" r="2.2" fill="#f4f1bd"/></svg><span>Level 12, 48 Harbour Lane,<br>Northvale, Victoria 3000<br>Australia</span></span></div>
  </div>
</footer>

<div class="copy">© 2017 Lorvin Medical. All Rights Reserved.</div>

</body>
</html>
```